Website redesign for a technology and engineering company

We'd like to redesign our website which can be found on quorvane.co.nz
!! Please find the designers brief as an uploaded file with all details in there!!
The main purpose for redesign is:
>change of services offered
>old website not very user friendly to maintain or update
Key requirements:
>visually appealing
>easy to navigate
>simple and easy to read
>responsive
>mobile device compatibility
>integrating best SEO practice
All the details are in the attached designer brief document.

```html
<!DOCTYPE html>
<html lang="en">
<head>
<meta charset="utf-8">
<title>Quorvane — Precision. Efficiency. Clarity.</title>
<link href="https://fonts.googleapis.com/css2?family=Urbanist:wght@400;500;600;700;800&display=swap" rel="stylesheet">
<style>
:root{
  --blue:#4f73ea;
  --blue-bright:#3f6af0;
  --navy:#0f1a3e;
  --navy-deep:#0b1433;
  --ink:#111111;
  --text:#222222;
  --muted:#8a8a8a;
  --line:#c9c9d3;
  --white:#ffffff;
}
*{box-sizing:border-box;margin:0;padding:0}
html,body{width:1200px;height:3945px;overflow:hidden}
body{position:relative;font-family:"Urbanist",sans-serif;color:var(--text);background:var(--white)}
.abs{position:absolute}
.ph{position:absolute;display:block}

/* hero */
.hero{left:0;top:0;width:1200px;height:533px;background:linear-gradient(180deg,#5b7bc4 0%,#3d5796 35%,#2c3b63 65%,#2a3352 100%)}
.brand{font-weight:700;color:var(--white);font-size:44px;letter-spacing:.5px;display:flex;align-items:center;gap:12px}
.brand .dot{width:16px;height:16px;border-radius:50%;background:var(--white)}
.hero .brand{left:141px;top:42px}
.btn-ghost{left:935px;top:46px;width:120px;height:41px;border:1.5px solid var(--white);border-radius:21px;color:var(--white);font-size:12px;font-weight:700;display:flex;align-items:center;justify-content:center}
.hero-title{left:0;width:1200px;top:296px;text-align:center;color:var(--white);font-size:42px;font-weight:800;letter-spacing:.5px}
.btn-solid{background:var(--blue-bright);color:var(--white);font-weight:700;font-size:14px;border-radius:24px;display:flex;align-items:center;justify-content:center;gap:8px}
.hero .btn-solid{left:539px;top:377px;width:122px;height:44px}
.pager{left:0;width:1200px;top:454px;display:flex;justify-content:center;align-items:center;gap:10px;color:var(--white);font-size:14px;font-weight:700}
.pager span{text-decoration:underline}
.pager i{display:block;width:18px;height:1px;background:var(--white)}

/* section heading */
.section-title{left:0;width:1200px;text-align:center;font-weight:700;font-size:35px;color:var(--ink)}
.divider{left:0;width:1200px;display:flex;justify-content:center;align-items:center;gap:8px}
.divider i{display:block;width:24px;height:2px;background:var(--ink)}
.divider b{display:block;width:10px;height:10px;border-radius:50%;border:2px solid var(--ink)}

/* about */
.about-frame{left:461px;top:934px;width:172px;height:150px;background:var(--white)}
.badge{left:479px;top:952px;width:132px;height:132px;background:var(--navy-deep);color:var(--white);text-align:center;padding-top:34px}
.badge strong{display:block;font-size:30px;font-weight:800;line-height:1}
.badge span{display:block;font-size:11px;line-height:14px;margin-top:6px}
.about-title{left:674px;top:690px;font-size:29px;font-weight:700;color:var(--ink)}
.about .divider{left:674px;width:auto;top:736px}
.about-text{left:672px;top:762px;width:390px;font-size:13.5px;line-height:25.5px;color:var(--ink);word-break:break-all}
.btn-outline{left:672px;top:958px;width:113px;height:40px;border:1.5px solid var(--ink);border-radius:20px;font-size:12.5px;font-weight:700;color:var(--ink);display:flex;align-items:center;justify-content:center}

/* services */
.services-band{left:0;top:1171px;width:1200px;height:577px;background:linear-gradient(180deg,#5478e8 0%,#4a70e6 100%)}
.services-title{color:var(--white);top:1233px}
.services .divider i{background:var(--white)}
.services .divider b{border-color:var(--white)}
.card{width:292px;height:622px;top:1348px;background:var(--white);box-shadow:0 6px 18px rgba(20,30,70,.12)}
.card .ph{left:0;top:0;width:100%;height:224px}
.card h3{position:absolute;left:28px;top:252px;font-size:19px;font-weight:700;color:var(--ink)}
.card ul{position:absolute;left:28px;top:296px;list-style:none}
.card li{font-size:12px;line-height:33.5px;color:var(--ink);padding-left:20px;position:relative}
.card li::before{content:"";position:absolute;left:0;top:15px;width:5px;height:5px;border-radius:50%;background:var(--ink)}

/* contact */
.field{left:194px;width:812px;height:55px;border:1.5px solid #b9b9c4;border-radius:28px;font-size:12px;color:#555;padding:21px 0 0 34px}
.field.active{border:2px solid var(--blue-bright);color:#9a9a9a}
.field.message{height:100px;border-radius:24px}
.field-label{left:233px;top:3000px;width:87px;height:23px;border-radius:12px;background:var(--blue-bright);color:var(--white);font-size:9px;display:flex;align-items:center;justify-content:center}
.form .btn-solid{left:551px;top:3441px;width:96px;height:40px;font-size:13px}

/* footer */
.footer{left:0;top:3566px;width:1200px;height:329px;background:linear-gradient(180deg,#141d42,#0d1636)}
.footer .brand{left:141px;top:3710px;font-size:42px}
.foot-col h4{font-size:16px;font-weight:700;color:var(--white);letter-spacing:.3px;margin-bottom:14px}
.foot-col p{font-size:12px;color:var(--white);line-height:24px}
.contact-row{display:flex;gap:10px;font-size:12px;color:var(--white);line-height:18px;margin-bottom:12px}
.contact-row svg{flex:none;margin-top:3px}
.news{left:826px;top:3702px;width:232px;height:41px;background:var(--white);border-radius:21px;font-size:11px;color:#777;padding:13px 0 0 14px}
.news-go{left:1023px;top:3708px;width:30px;height:30px;border-radius:50%;background:var(--blue-bright);display:flex;align-items:center;justify-content:center}
.copyright{left:0;top:3895px;width:1200px;height:50px;background:var(--blue-bright);color:var(--white);font-size:12px;display:flex;align-items:center;justify-content:center}
</style>
</head>
<body>

<header class="hero abs" role="img" aria-label="Mountain ridge at dusk with a solar powered GNSS and antenna monitoring station"></header>
<div class="brand abs" style="left:141px;top:42px">Quorvane</div>
<a class="btn-ghost abs">Get in touch</a>
<h1 class="hero-title abs">PRECISION.EFFICIENCY.CLARITY.</h1>
<div class="hero"><a class="btn-solid abs" style="left:539px;top:377px;width:122px;height:44px">Contact Us</a></div>
<div class="pager abs"><span>01</span><i></i><span>02</span><i></i><span>03</span></div>

<section class="about">
  <div class="ph" style="left:141px;top:621px;width:453px;height:454px;background:linear-gradient(180deg,#c9ccd2 0%,#b4b9c0 35%,#6f9a4a 55%,#4d7a35 100%)" role="img" aria-label="Hilltop GNSS stations and a utility vehicle on green grass under cloud"></div>
  <div class="about-frame abs"></div>
  <div class="badge abs"><strong>15+</strong><span>Years<br>of Experience</span></div>
  <h2 class="about-title abs">About Us</h2>
  <div class="divider abs"><i></i><b></b><i></i></div>
  <p class="about-text abs">Welcome to Quorvane, your reliable partner in delivering innovative solutions. Our team of skilled professionals is committed to excellence, ensuring every project is handled with precision, efficiency,andintegrity.Wesolveproblemsinthefield,buildrobustinfrastructure,anddeliveraccuratedatatoourclients.Letus helpyouachieveyourgoalswithourtailored</p>
  <a class="btn-outline abs">Get Started</a>
</section>

<section class="services">
  <div class="services-band abs" role="img" aria-label="Blue tinted backdrop of a communications mast in the snow"></div>
  <div class="ph" style="left:934px;top:1079px;width:199px;height:184px;background:radial-gradient(ellipse at center,#4a5560 0%,#3a444d 55%,rgba(255,255,255,0) 72%)" role="img" aria-label="Rugged grey network enclosure with ethernet port"></div>
  <h2 class="section-title services-title abs" style="color:#fff">Our Services</h2>
  <div class="divider abs" style="top:1290px"><i></i><b></b><i></i></div>

  <article class="card abs" style="left:141px">
    <div class="ph" style="background:linear-gradient(180deg,#7fa8d8 0%,#5c7f9e 45%,#c8352e 70%,#8a1f1d 100%)" role="img" aria-label="Field equipment case aboard a red inflatable boat near a rocky coast"></div>
    <h3>Fieldwork Solutions</h3>
    <ul>
      <li>Project management &amp; logistics</li>
      <li>Efficient product rollouts</li>
      <li>Equipment Installation &amp; Maintenance</li>
      <li>SurveyingTechniques</li>
      <li>Precision GNSS instrumentation</li>
      <li>Seismic Instrumentation</li>
      <li>IOT Sensors</li>
      <li>Reliable Communications Systems</li>
      <li>Environmental sensors</li>
    </ul>
  </article>

  <article class="card abs" style="left:455px">
    <div class="ph" style="background:linear-gradient(180deg,#c5ccd4 0%,#8b97a0 40%,#8d8a55 70%,#7a6d3c 100%)" role="img" aria-label="GNSS base station on a grassy hill above a valley"></div>
    <h3>Positioning And Monitoring</h3>
    <ul>
      <li>Real-Time Kinematic (RTK) Solutions</li>
      <li>Custom GNSS Base stations</li>
      <li>NTRIP service</li>
      <li>Tailored Monitoring Solutions</li>
      <li>Environmental Monitoring</li>
      <li>Robust communication Systems</li>
      <li>Internet of Things (IoT) Integration</li>
      <li>Solar powered systems</li>
      <li>Smart Sensor Networks</li>
    </ul>
  </article>

  <article class="card abs" style="left:765px">
    <div class="ph" style="background:linear-gradient(135deg,#e8e8ea 0%,#c9cacd 50%,#9a9ca0 100%)" role="img" aria-label="Machined parts and calipers resting on engineering drawings"></div>
    <h3>Design And Prototyping</h3>
    <ul>
      <li>Mechanical Component Design</li>
      <li>Robust Field Equipment Infrastructure</li>
      <li>Remote Monitoring System Design</li>
      <li>3D modelling</li>
      <li>Standalone Power Solutions</li>
      <li>Wireless Communication Solutions</li>
      <li>Real-Time Data Transmission</li>
      <li>Rapid Prototyping</li>
      <li>Field Deployment and Testing</li>
    </ul>
  </article>
</section>

<section class="projects">
  <h2 class="section-title abs" style="top:2052px">Project Cases</h2>
  <div class="divider abs" style="top:2107px"><i></i><b></b><i></i></div>

  <div class="ph" style="left:0;top:2172px;width:344px;height:305px;background:linear-gradient(180deg,#b9c6d6 0%,#d5d9de 35%,#7c9a4f 65%,#6d7d3a 100%)" role="img" aria-label="Survey instrument on a tripod in a field with a radio telescope dish behind"></div>
  <div class="ph" style="left:0;top:2498px;width:344px;height:305px;background:linear-gradient(180deg,#8fb0d6 0%,#5f8a4c 40%,#c9cbc9 65%,#5c5a4d 100%)" role="img" aria-label="Equipment hut with satellite dish behind a wooden fence"></div>
  <div class="ph" style="left:372px;top:2172px;width:239px;height:386px;background:linear-gradient(180deg,#3b79d6 0%,#6a9ae0 60%,#9fb8d8 100%)" role="img" aria-label="Technician climbing a telecommunications tower with microwave dishes"></div>
  <div class="ph" style="left:372px;top:2584px;width:239px;height:219px;background:linear-gradient(180deg,#d8b98a 0%,#b89868 50%,#3a3a3a 100%)" role="img" aria-label="Electrical control panel with breakers and a solar charge controller"></div>
  <div class="ph" style="left:638px;top:2172px;width:239px;height:243px;background:linear-gradient(180deg,#8e8d7a 0%,#b6b3a6 45%,#6c7356 100%)" role="img" aria-label="Aerial view of a rocky creek beside a ladder track"></div>
  <div class="ph" style="left:638px;top:2441px;width:239px;height:362px;background:linear-gradient(180deg,#4f7fd4 0%,#8aa8d8 35%,#d0d2d2 60%,#3e4a2f 100%)" role="img" aria-label="Technician on a ladder installing a dish on an equipment hut"></div>
  <div class="ph" style="left:905px;top:2172px;width:295px;height:305px;background:linear-gradient(180deg,#3f63c8 0%,#7a94cc 45%,#9a9890 75%,#6b6a62 100%)" role="img" aria-label="Solar powered monitoring station on rocky alpine ground"></div>
  <div class="ph" style="left:905px;top:2498px;width:295px;height:305px;background:linear-gradient(180deg,#8faad6 0%,#b9bcbf 35%,#8a6f58 65%,#5d4a3c 100%)" role="img" aria-label="Rusted railway tracks and timbers near a bridge"></div>
</section>

<section class="form">
  <h2 class="section-title abs" style="top:2890px">Get in touch with us!</h2>
  <div class="divider abs" style="top:2944px"><i></i><b></b><i></i></div>
  <div class="field active abs" style="top:3015px">Name</div>
  <div class="field-label abs">Your Name</div>
  <div class="field abs" style="top:3090px">Subject</div>
  <div class="field abs" style="top:3165px">Phone No</div>
  <div class="field abs" style="top:3240px">Email Address</div>
  <div class="field message abs" style="top:3315px">Massage</div>
  <a class="btn-solid abs">Send
    <svg width="14" height="14" viewBox="0 0 14 14"><path d="M1 1 L13 7 L1 13 L3 7 Z" fill="#fff"/></svg>
  </a>
</section>

<footer>
  <div class="footer abs"></div>
  <div class="brand abs" style="left:141px;top:3710px;font-size:42px">Quorvane</div>

  <div class="foot-col abs" style="left:377px;top:3656px">
    <h4>RESOURCES</h4>
    <p>Privacy Policy</p>
    <p>Terms of Service</p>
    <p>Contact</p>
  </div>

  <div class="foot-col abs" style="left:569px;top:3656px">
    <h4>CONTACT DETAILS</h4>
    <div class="contact-row">
      <svg width="11" height="14" viewBox="0 0 11 14"><path d="M5.5 0C2.5 0 0 2.4 0 5.4 0 9.3 5.5 14 5.5 14S11 9.3 11 5.4C11 2.4 8.5 0 5.5 0Zm0 7.5a2 2 0 1 1 0-4 2 2 0 0 1 0 4Z" fill="#fff"/></svg>
      <span>Lorem Ipsum is simply dummy text</span>
    </div>
    <div class="contact-row">
      <svg width="12" height="12" viewBox="0 0 12 12"><path d="M2.4 0.5 4.3 2.6 3.4 4.1C4.1 5.6 6.2 7.8 7.8 8.6L9.3 7.7 11.5 9.6 10.2 11.5C5.3 11.3 0.7 6.6 0.5 1.8Z" fill="#fff"/></svg>
      <span>Phone<br>+64 21 555 0198</span>
    </div>
    <div class="contact-row">
      <svg width="13" height="10" viewBox="0 0 13 10"><rect x="0.5" y="0.5" width="12" height="9" fill="none" stroke="#fff"/><path d="M0.5 0.5 6.5 5.5 12.5 0.5" fill="none" stroke="#fff"/></svg>
      <span>Email<br>hi@quorvane.nz</span>
    </div>
  </div>

  <div class="foot-col abs" style="left:825px;top:3656px">
    <h4>NEWSLETTER</h4>
  </div>
  <div class="news abs">Enter your email</div>
  <div class="news-go abs">
    <svg width="12" height="12" viewBox="0 0 12 12"><path d="M1 1 L11 6 L1 11 L3 6 Z" fill="#fff"/></svg>
  </div>

  <div class="copyright abs">Copyright © Quorvane 2024. All Rights Reserved.</div>
</footer>

</body>
</html>
```